Food Safety Consultancy Flyer Design

We need a flyer design for a new company called Tundo Training. New food safety regulations are coming into effect for all food operators in March 2016. My company provides training and resources to support food operators during the transition onto the new Food Control Plan. For the designs we would like to see any of the colours used from the logo which is attached. The flyer will be letting operators know that there are new regulations and we are here to help. Our company offers three packages: 1. Videos (training videos) 2. Webinars and Workshop 3. One-on-one mentoring. Our websites main colour used is the green colour from the logo.
Food service operators: cafes, restaurants etc.
Hospitality

```html
<!DOCTYPE html>
<html lang="en">
<head>
<meta charset="utf-8">
<title>Tundo Training – Food Act 2014 Flyer</title>
<link rel="stylesheet" href="https://fonts.googleapis.com/css2?family=Roboto+Condensed:wght@400;700&family=Lato:wght@400;700&display=swap">
<style>
  :root {
    --green: #3cb44b;
    --blue: #1f72c0;
    --dark: #262626;
    --dark-2: #3b3b3b;
    --white: #ffffff;
    --ink: #222222;
  }
  * { margin: 0; padding: 0; box-sizing: border-box; }
  html, body { width: 907px; height: 1200px; overflow: hidden; background: var(--white); }
  .flyer {
    position: relative; width: 907px; height: 1200px; overflow: hidden;
    font-family: "Lato", Arial, sans-serif; color: var(--ink); background: var(--white);
  }
  .hero-photo {
    position: absolute; left: 0; top: 0; width: 907px; height: 400px;
    background:
      radial-gradient(ellipse at 30% 80%, #6f7d3a 0%, transparent 45%),
      radial-gradient(ellipse at 75% 80%, #b0502c 0%, transparent 40%),
      linear-gradient(180deg, #8c8479 0%, #d9d2c6 35%, #7a6a55 75%, #3f3226 100%);
  }
  .headline-band {
    position: absolute; left: 0; top: 400px; width: 907px; height: 180px;
    background: linear-gradient(180deg, #1c1c1c 0%, var(--dark-2) 50%, #1c1c1c 100%);
    border-top: 6px solid var(--green);
    border-bottom: 6px solid var(--green);
  }
  .footer-band {
    position: absolute; left: 0; top: 1104px; width: 907px; height: 96px;
    background: var(--dark); border-top: 6px solid var(--green);
  }
  .brand-tab {
    position: absolute; left: 278px; top: 0; width: 350px; height: 118px;
    background: var(--white); border-radius: 0 0 18px 18px;
    display: flex; align-items: center; justify-content: center; gap: 12px;
  }
  .brand-dot { width: 22px; height: 22px; border-radius: 50%; background: var(--green); }
  .brand-name {
    font-family: "Roboto Condensed", Arial, sans-serif; font-weight: 700;
    font-size: 38px; letter-spacing: 1px; color: var(--dark);
  }
  .headline {
    position: absolute; left: 0; width: 907px; top: 438px; text-align: center;
    font-family: "Roboto Condensed", Arial, sans-serif; font-weight: 700;
    font-size: 44px; color: var(--green); letter-spacing: 0.5px;
  }
  .headline-date {
    position: absolute; left: 0; width: 907px; top: 494px; text-align: center;
    font-family: "Roboto Condensed", Arial, sans-serif; font-weight: 700;
    font-size: 33px; color: var(--white);
  }
  .intro {
    position: absolute; left: 0; width: 907px; top: 604px; text-align: center;
    font-size: 17.5px; line-height: 25px;
  }
  .slogan {
    position: absolute; left: 130px; top: 664px; width: 647px; height: 50px;
    background: var(--blue); border-radius: 25px; color: var(--white);
    font-family: "Roboto Condensed", Arial, sans-serif; font-weight: 700; font-size: 29px;
    display: flex; align-items: center; justify-content: center;
  }
  .knowledge-title {
    position: absolute; left: 0; width: 907px; top: 722px; text-align: center;
    font-family: "Roboto Condensed", Arial, sans-serif; font-weight: 700; font-size: 27px;
  }
  .knowledge-list { position: absolute; list-style: none; font-size: 18px; line-height: 25px; }
  .knowledge-list li { position: relative; padding-left: 18px; }
  .knowledge-list li::before {
    content: ""; position: absolute; left: 2px; top: 9px; width: 8px; height: 8px;
    border-radius: 50%; background: var(--green);
  }
  .knowledge-list.left { left: 150px; top: 770px; }
  .knowledge-list.right { left: 530px; top: 765px; }
  .packages-title {
    position: absolute; left: 328px; top: 844px; width: 252px; height: 36px;
    background: var(--blue); border-radius: 18px; color: var(--white);
    font-family: "Roboto Condensed", Arial, sans-serif; font-weight: 700; font-size: 24px;
    display: flex; align-items: center; justify-content: center;
  }
  .package {
    position: absolute; top: 897px; height: 188px; border-radius: 14px;
    text-align: center; color: var(--white); font-size: 17.5px; line-height: 23px; padding: 10px 14px;
  }
  .package h3 {
    font-family: "Roboto Condensed", Arial, sans-serif; font-weight: 700; font-size: 19px;
    color: var(--dark); margin-bottom: 4px;
  }
  .package.videos { left: 24px; width: 278px; background: var(--green); }
  .package.webinars { left: 312px; width: 283px; background: var(--dark); padding: 10px 26px; }
  .package.webinars h3 { color: var(--green); }
  .package.mentoring { left: 603px; width: 280px; background: var(--green); padding: 10px 26px; }
  .package.mentoring h3 { margin: 8px 0 22px; }
  .contact {
    position: absolute; left: 0; width: 907px; top: 1140px;
    display: flex; justify-content: center; gap: 70px; color: var(--white); font-size: 24px;
  }
  .contact span { display: flex; align-items: center; gap: 10px; }
</style>
</head>
<body>
<div class="flyer">
  <div class="hero-photo" role="img" aria-label="Photo of caterers serving plated vegetables and grilled dishes at a buffet"></div>
  <div class="headline-band"></div>
  <div class="footer-band"></div>

  <div class="brand-tab">
    <span class="brand-dot"></span>
    <span class="brand-name">Tundo Training</span>
  </div>

  <h1 class="headline">THE FOOD ACT 2014 COMES INTO FORCE</h1>
  <p class="headline-date">ON 1 MARCH 2016</p>

  <p class="intro">and risk management to produce safe and suitable food<br>Food service and food retailers will be on Food Control Plans – documentation of processes</p>

  <div class="slogan">Tundo Training – Your reputation is our business</div>

  <h2 class="knowledge-title">With up-to-date knowledge on</h2>
  <ul class="knowledge-list left">
    <li>The Food Act 2014</li>
    <li>Food Control Plan<br>requirements</li>
  </ul>
  <ul class="knowledge-list right">
    <li>Verification expectations</li>
    <li>New Food Grading system</li>
    <li>New Fees</li>
  </ul>

  <div class="packages-title">Our Packages</div>

  <section class="package videos">
    <h3>Videos</h3>
    <p>Animated training videos<br>of the FCP<br>6 month subscription<br>Translated into Mandarin<br>Japanese, Korean<br>and Hindi</p>
  </section>
  <section class="package webinars">
    <h3>Webinars/Workshops</h3>
    <p>A range of webinars at times to suit the hospitality industry AND half day training workshops. 6 month subscription to the video</p>
  </section>
  <section class="package mentoring">
    <h3>One-to-one mentoring</h3>
    <p>We come to you and go through the FCP page-by-page</p>
  </section>

  <div class="contact">
    <span>
      <svg width="16" height="16" viewBox="0 0 16 16" aria-hidden="true"><circle cx="8" cy="8" r="7" fill="none" stroke="var(--green)" stroke-width="1.6"/><ellipse cx="8" cy="8" rx="3" ry="7" fill="none" stroke="var(--green)" stroke-width="1.4"/><line x1="1" y1="8" x2="15" y2="8" stroke="var(--green)" stroke-width="1.4"/></svg>
      www.tundotraining.co.nz
    </span>
    <span>
      <svg width="20" height="14" viewBox="0 0 20 14" aria-hidden="true"><rect x="0" y="0" width="20" height="14" rx="1" fill="var(--green)"/><path d="M0 0 L10 8 L20 0" fill="none" stroke="var(--dark)" stroke-width="1.6"/></svg>
      info@tundotraining.co.nz
    </span>
  </div>
</div>
</body>
</html>
```